Brintell's Business Card

I need some designs for a new business card including the new logo attached. An old example of our business card is also attached to show all the data that should be included on the new design.
**I added some more examples someone had mocked up**

Contact Information for Business Card

Should include all info on other examples uploaded.

```html
<!DOCTYPE html>
<html lang="en">
<head>
<meta charset="utf-8">
<title>Brintell's Business Card</title>
<link rel="stylesheet" href="https://fonts.googleapis.com/css2?family=Libre+Baskerville:wght@700&family=Montserrat:wght@600&family=Open+Sans:wght@400;600&display=swap">
<style>
  :root {
    --page: #e9e6e1;
    --card-white: #ffffff;
    --charcoal: #353535;
    --brand-blue: #1a6fc0;
    --brand-red: #e42320;
    --ink: #111111;
    --band-text: #f2f2f2;
  }
  * { margin: 0; padding: 0; box-sizing: border-box; }
  html, body {
    width: 1200px; height: 1000px; overflow: hidden;
    background: var(--page);
  }
  .sheet {
    position: relative; width: 1200px; height: 1000px;
  }
  .card {
    position: absolute; left: 250px; width: 700px; height: 400px;
    overflow: hidden; box-shadow: 0 6px 18px rgba(0,0,0,.18);
  }
  /* front */
  .card-front { top: 50px; background: var(--card-white); }
  .brand-block {
    position: absolute; left: 0; top: 0; width: 300px; height: 300px;
    display: flex; align-items: center; justify-content: center; gap: 10px;
  }
  .brand-mark {
    width: 22px; height: 22px; background: var(--brand-red);
  }
  .brand-name {
    font-family: "Montserrat", sans-serif; font-weight: 600;
    font-size: 38px; color: var(--brand-blue); letter-spacing: .5px;
  }
  .divider {
    position: absolute; left: 300px; top: 40px; width: 2px; height: 250px;
    background: var(--ink);
  }
  .holder-name {
    position: absolute; left: 350px; top: 70px;
    font-family: "Libre Baskerville", serif; font-weight: 700;
    font-size: 26px; color: var(--ink);
    display: flex; align-items: flex-end;
  }
  .name-accent {
    display: inline-block; width: 26px; height: 9px; margin-left: 2px; margin-bottom: 4px;
    background: var(--brand-red);
  }
  .contact-list {
    position: absolute; right: 40px; top: 165px; list-style: none;
    font-family: "Open Sans", sans-serif; font-size: 17px; color: var(--ink);
  }
  .contact-item {
    display: flex; justify-content: flex-end; align-items: center; gap: 10px;
    margin-bottom: 9px;
  }
  .contact-icon {
    width: 19px; height: 19px; background: var(--brand-red);
    display: flex; align-items: center; justify-content: center;
  }
  .info-band {
    position: absolute; left: 0; bottom: 0; width: 100%; height: 100px;
    background: var(--charcoal);
    font-family: "Open Sans", sans-serif; font-weight: 600;
    font-size: 17px; color: var(--band-text); letter-spacing: .5px;
  }
  .band-left { position: absolute; left: 40px; top: 10px; }
  .band-right { position: absolute; right: 40px; bottom: 14px; }
  /* back */
  .card-back {
    top: 530px; background: var(--charcoal);
    display: flex; align-items: center; justify-content: center; gap: 14px;
  }
  .card-back .brand-mark { width: 30px; height: 30px; border-radius: 50%; }
  .card-back .brand-name { font-size: 60px; }
</style>
</head>
<body>
<main class="sheet">
  <section class="card card-front" aria-label="Business card front">
    <div class="brand-block">
      <span class="brand-mark"></span>
      <span class="brand-name">Brintell's</span>
    </div>
    <div class="divider"></div>
    <h1 class="holder-name">Wesley Brintell<span class="name-accent"></span></h1>
    <ul class="contact-list">
      <li class="contact-item">555.014.2287
        <span class="contact-icon">
          <svg width="13" height="13" viewBox="0 0 24 24"><path fill="#fff" d="M6.6 10.8a15 15 0 0 0 6.6 6.6l2.2-2.2c.3-.3.7-.4 1-.2 1.1.4 2.3.6 3.6.6.6 0 1 .4 1 1V20c0 .6-.4 1-1 1A17 17 0 0 1 3 4c0-.6.4-1 1-1h3.5c.6 0 1 .4 1 1 0 1.3.2 2.5.6 3.6.1.3 0 .7-.2 1z"/></svg>
        </span>
      </li>
      <li class="contact-item">hvacbrintell@mailbox.com
        <span class="contact-icon">
          <svg width="13" height="13" viewBox="0 0 24 24"><path fill="#fff" d="M2 5h20v14H2z"/><path fill="none" stroke="#e42320" stroke-width="2" d="M2 6l10 7 10-7"/></svg>
        </span>
      </li>
    </ul>
    <div class="info-band">
      <span class="band-left">LICENSED &amp; INSURED</span>
      <span class="band-right">FAMILY OWNED &amp; OPERATED</span>
    </div>
  </section>

  <section class="card card-back" aria-label="Business card back">
    <span class="brand-mark"></span>
    <span class="brand-name">Brintell's</span>
  </section>
</main>
</body>
</html>
```